Business Card

The design you sent was fine. I just need the logo changed on one side. The back needs to have the text "Vell Marrow Group" next to the log and the words "Insight Strategy Guidance" in the middle. The front logo needs to have the "Vell Marrow Advisory" logo attached

Colors

Designer to choose colors to be used in the design.

```html
<!DOCTYPE html>
<html lang="en">
<head>
<meta charset="utf-8">
<title>Vell Marrow Business Card</title>
<link href="https://fonts.googleapis.com/css2?family=Lato:ital,wght@0,400;0,700;0,900;1,400&display=swap" rel="stylesheet">
<style>
  :root {
    --stage: #202020;
    --cyan: #00b2d8;
    --ink: #111111;
    --paper: #ffffff;
    --muted: #222222;
  }
  * { margin: 0; padding: 0; box-sizing: border-box; }
  html, body { width: 1200px; height: 878px; overflow: hidden; }
  body {
    background: var(--stage);
    font-family: "Lato", sans-serif;
    display: flex;
    flex-direction: column;
    align-items: center;
    justify-content: center;
    gap: 40px;
  }
  .card {
    width: 600px;
    height: 343px;
    position: relative;
    overflow: hidden;
  }

  /* Back side */
  .card-back {
    background: var(--cyan);
    display: flex;
    align-items: center;
    justify-content: center;
  }
  .back-brand { display: flex; align-items: center; gap: 18px; }
  .brand-square {
    width: 70px; height: 70px;
    background: var(--ink);
    border: 4px solid var(--paper);
    flex: none;
  }
  .back-name {
    font-weight: 700;
    font-size: 40px;
    color: var(--ink);
    line-height: 1;
  }
  .back-tagline {
    font-size: 15px;
    color: var(--ink);
    margin-top: 6px;
    letter-spacing: 0.5px;
  }

  /* Front side */
  .card-front { background: var(--paper); }
  .holder { position: absolute; left: 30px; top: 34px; }
  .holder-name {
    font-weight: 900;
    font-size: 27px;
    color: var(--cyan);
    letter-spacing: 0.3px;
    line-height: 1;
  }
  .holder-role {
    font-style: italic;
    font-size: 16px;
    color: var(--muted);
    margin-top: 2px;
  }
  .front-brand {
    position: absolute; right: 38px; top: 118px;
    display: flex; align-items: center; gap: 12px;
  }
  .brand-circle {
    width: 48px; height: 48px;
    border-radius: 50%;
    background: var(--cyan);
    flex: none;
  }
  .front-name {
    font-weight: 700;
    font-size: 26px;
    color: var(--ink);
    line-height: 1.05;
    white-space: nowrap;
  }
  .front-tagline {
    font-size: 8px;
    font-weight: 700;
    color: var(--ink);
    margin-top: 6px;
    white-space: nowrap;
  }
  .contacts {
    position: absolute; left: 40px; top: 196px;
    list-style: none;
  }
  .contacts li {
    display: flex; align-items: center; gap: 12px;
    font-size: 17px; color: var(--ink);
    height: 24px;
  }
  .contacts svg { width: 14px; height: 14px; fill: var(--cyan); flex: none; }
  .address-rule {
    position: absolute; left: 30px; right: 40px; top: 274px;
    border-top: 1px solid var(--cyan);
  }
  .address {
    position: absolute; left: 30px; top: 282px;
    display: flex; align-items: center; gap: 12px;
    font-size: 17px; color: var(--ink);
  }
  .address svg { width: 13px; height: 16px; fill: var(--cyan); }
  .base-band {
    position: absolute; left: 0; right: 0; bottom: 0; height: 18px;
    background: var(--cyan);
  }
  .base-band::before {
    content: ""; position: absolute; left: 0; top: 0;
    width: 38px; height: 100%; background: var(--ink);
    border-right: 5px solid var(--paper);
  }
</style>
</head>
<body>

<section class="card card-back" aria-label="Card back">
  <div class="back-brand">
    <div class="brand-square"></div>
    <div>
      <div class="back-name">Vell Marrow Group</div>
      <div class="back-tagline">Insight Strategy Guidance</div>
    </div>
  </div>
</section>

<section class="card card-front" aria-label="Card front">
  <div class="holder">
    <div class="holder-name">ALAN CORDE</div>
    <div class="holder-role">Founder &amp; CEO</div>
  </div>

  <div class="front-brand">
    <div class="brand-circle"></div>
    <div>
      <div class="front-name">Vell Marrow Advisory</div>
      <div class="front-tagline">Clear Thinking delivering Practical Results Daily</div>
    </div>
  </div>

  <ul class="contacts">
    <li>
      <svg viewBox="0 0 24 24"><path d="M6.6 10.8a15 15 0 0 0 6.6 6.6l2.2-2.2a1 1 0 0 1 1-.25 11.4 11.4 0 0 0 3.6.57 1 1 0 0 1 1 1V20a1 1 0 0 1-1 1A17 17 0 0 1 3 4a1 1 0 0 1 1-1h3.5a1 1 0 0 1 1 1c0 1.25.2 2.45.57 3.57a1 1 0 0 1-.25 1z"/></svg>
      1234567890
    </li>
    <li>
      <svg viewBox="0 0 24 24"><path d="M2 5h20v14H2zm2 2v.5l8 5 8-5V7l-8 5z"/></svg>
      info@yourmail.com
    </li>
    <li>
      <svg viewBox="0 0 24 24"><path d="M12 2a10 10 0 1 0 0 20 10 10 0 0 0 0-20zm0 2c.9 1.2 1.6 2.9 1.9 5h-3.8c.3-2.1 1-3.8 1.9-5zM4.3 13a8 8 0 0 1 0-2h3.8a18 18 0 0 0 0 2zm5.8 0a16 16 0 0 1 0-2h3.8a16 16 0 0 1 0 2zm5.8 0a18 18 0 0 0 0-2h3.8a8 8 0 0 1 0 2zm-5.8 2h3.8c-.3 2.1-1 3.8-1.9 5-.9-1.2-1.6-2.9-1.9-5z"/></svg>
      www.yourwebsite.com
    </li>
  </ul>

  <div class="address-rule"></div>
  <div class="address">
    <svg viewBox="0 0 24 30"><path d="M12 0A12 12 0 0 0 0 12c0 9 12 18 12 18s12-9 12-18A12 12 0 0 0 12 0zm0 16a4 4 0 1 1 0-8 4 4 0 0 1 0 8z"/></svg>
    1234 First Line Address 5678 Second Line Address
  </div>

  <div class="base-band"></div>
</section>

</body>
</html>
```